beauty/party

I have both my designs from pixel harbor. double sided business card needed and incorporate other information. although I have my designs I don't do things by halves so im wanting people to say nice cards. first impression best impression. On the Wattle mobile skin and beauty side I want in bullet point the following: Facials, Microdermabrasion, Oxygen Infusion, Peels, Dermaroller . tinting & Adult Pamper Parties. I also want the healthier looking skin removed!! and I want the words love your skin wth a Heart with the word love in it. but not under my logo. somewhere else. If possible!! On the Little Velvet Fern side I want the words Childrens Pamper, Ballet, Hip Hop & High Tea Parties. I need the number 0499 57 3816 used on both sides and www.littlevelvetfern.com.au on little velvet fern side. If you don't understand my instructions you are welcome to message me. Please use the white background

```html
<!DOCTYPE html>
<html lang="en">
<head>
<meta charset="utf-8">
<title>Little Velvet Fern &amp; Wattle mobile skin and beauty – business cards</title>
<link href="https://fonts.googleapis.com/css2?family=Source+Sans+3:wght@400;600;700&display=swap" rel="stylesheet">
<style>
  :root {
    --backdrop: #4a3d35;
    --card: #ffffff;
    --card-shade: #eef0f2;
    --pink: #e6137f;
    --plum: #7a1f4f;
    --rose: #d9649f;
    --rose-soft: #f3b6d3;
    --yellow: #f2e600;
    --yellow-edge: #b8ac00;
    --ink: #3c3c3c;
    --ink-soft: #555555;
  }
  * { box-sizing: border-box; margin: 0; padding: 0; }
  html, body {
    width: 1200px; height: 469px; overflow: hidden;
    background: var(--backdrop);
    font-family: "Source Sans 3", "Myriad Pro", Arial, sans-serif;
  }
  .stage { position: relative; width: 1200px; height: 469px; }

  .card {
    position: absolute; top: 104px;
    width: 464px; height: 264px;
    background: linear-gradient(to bottom, var(--card) 35%, var(--card-shade) 100%);
    box-shadow: 0 4px 10px rgba(0,0,0,.35);
    overflow: hidden;
  }
  .card--party { left: 90px; }
  .card--skin  { left: 596px; }

  .rule { position: absolute; height: 3px; background: var(--pink); }

  /* party side */
  .name-tab {
    position: absolute; left: 0; top: 38px;
    width: 226px; height: 26px;
    background: var(--pink);
    border-radius: 0 13px 13px 0;
    color: #fff; font-size: 20px; font-weight: 400;
    line-height: 26px; padding-left: 24px;
    box-shadow: 0 2px 3px rgba(0,0,0,.2);
  }
  .activity-list {
    position: absolute; left: 24px; top: 174px;
    list-style: none; font-size: 12.5px; color: var(--ink);
  }
  .activity-list li { display: flex; align-items: center; height: 15px; }
  .activity-list .dot {
    width: 9px; height: 9px; border-radius: 50%;
    background: var(--yellow); border: 1px solid var(--yellow-edge);
    margin-right: 5px; flex: none;
  }
  .activity-list .dot--inline { margin-left: 9px; }
  .rule--party-left  { left: 22px;  top: 223px; width: 182px; }
  .rule--party-right { left: 216px; top: 223px; width: 216px; }
  .party-phone {
    position: absolute; left: 24px; top: 230px;
    font-size: 16px; font-weight: 600; color: var(--ink-soft);
  }
  .party-mascot {
    position: absolute; left: 340px; top: 92px;
    width: 94px; height: 84px; border-radius: 42px;
    background: radial-gradient(circle at 42% 55%, var(--yellow) 0 48%, #f7f2a8 70%, rgba(255,255,255,0) 72%);
  }
  .party-brand {
    position: absolute; left: 216px; top: 184px;
    font-size: 27px; font-weight: 700; color: var(--pink);
    line-height: 1; white-space: nowrap;
  }
  .party-web {
    position: absolute; left: 218px; top: 232px;
    font-size: 13px; letter-spacing: .8px; color: var(--ink-soft);
  }

  /* skin side */
  .skin-portrait {
    position: absolute; left: 82px; top: 52px;
    width: 104px; height: 104px;
    background: linear-gradient(135deg, var(--rose-soft), var(--pink) 60%, var(--rose));
    border: 3px solid #cfcfcf;
  }
  .skin-brand {
    position: absolute; left: 14px; top: 166px; width: 240px;
    font-size: 19px; font-weight: 400; color: var(--plum);
    text-align: center; line-height: 1.1;
  }
  .service-list {
    position: absolute; left: 290px; top: 44px;
    list-style: none; font-size: 12.5px; color: var(--plum);
  }
  .service-list li { display: flex; align-items: center; height: 17px; }
  .service-list li::before {
    content: ""; width: 7px; height: 7px; border-radius: 50%;
    background: var(--pink); margin-right: 7px; flex: none;
  }
  .skin-phone {
    position: absolute; left: 290px; top: 190px;
    font-size: 16px; font-weight: 600; color: var(--plum);
  }
  .rule--skin { left: 0; top: 223px; width: 464px; }
  .love-line {
    position: absolute; left: 0; top: 228px; width: 464px; height: 32px;
    display: flex; align-items: center; justify-content: center; gap: 6px;
    font-size: 17px; color: var(--plum);
  }
  .love-heart { width: 40px; height: 32px; display: block; }
</style>
</head>
<body>
<main class="stage">

  <section class="card card--party" aria-label="Little Velvet Fern card">
    <div class="name-tab">Little Velvet Fern</div>

    <ul class="activity-list">
      <li><span class="dot"></span>Children's Pamper</li>
      <li><span class="dot"></span>Ballet<span class="dot dot--inline"></span>Hip Hop</li>
      <li><span class="dot"></span>High Tea Parties</li>
    </ul>

    <div class="rule rule--party-left"></div>
    <p class="party-phone">tel: 0499 57 3816</p>

    <div class="party-mascot" role="img" aria-label="Illustrated mascot with a small crown"></div>
    <p class="party-brand">Little Velvet Fern</p>
    <div class="rule rule--party-right"></div>
    <p class="party-web">www.littlevelvetfern.com.au</p>
  </section>

  <section class="card card--skin" aria-label="Wattle mobile skin and beauty card">
    <div class="skin-portrait" role="img" aria-label="Pink square illustration of a woman's flowing hair"></div>
    <p class="skin-brand">Wattle mobile skin and beauty</p>

    <ul class="service-list">
      <li>Facials</li>
      <li>Microdermabrasion</li>
      <li>Oxygen Infusion</li>
      <li>Peels</li>
      <li>Dermaroller</li>
      <li>Tinting</li>
      <li>Adult Pamper Parties</li>
    </ul>

    <p class="skin-phone">tel: 0499 57 3816</p>

    <div class="rule rule--skin"></div>
    <div class="love-line">
      <svg class="love-heart" viewBox="0 0 40 32" role="img" aria-label="Heart with the word love">
        <path d="M20 31 C8 22 1 16 1 9 C1 4 5 1 10 1 C14 1 17 3 20 7 C23 3 26 1 30 1 C35 1 39 4 39 9 C39 16 32 22 20 31 Z" fill="#e6137f"/>
        <text x="20" y="17" text-anchor="middle" font-family="Source Sans 3, sans-serif" font-size="11" font-weight="600" fill="#ffffff">love</text>
      </svg>
      <span>your skin</span>
    </div>
  </section>

</main>
</body>
</html>
```